Label designs for a new company manufacturing food supplements bottles and containers

The design must reflect SPIRITUAL as well as PHYSICAL THERAPEUTIC BENEFITS ,Our company BRIGHTWATER HERBALIST produces Food Supplements products line. Such as vitamins, herbs, super foods,alkalizing , weight loss and amino acids these products are made of , pills, capsules, powders and liquids. The containers are of different sizes , small , medium and large . We need a contemporary label design that represents alternative approaches to physical and spiritual healing . Labels should exude trust worthiness, character, and quality to achieve optimum customer confidence.

Target Market(s)

People of age 25 & up , 50% female 50% Male

Industry/Entity Type

Alternative Medicine

Font styles to use
Serif

Requirements
Must have
• name of company, name of product , slogan or short description for people to understand what the product is all about . supplement facts, ingredient list, directions, statements , place of production, expiration and lot numbers.
Nice to have
• Easily recognizable corporate identity for optimum brand identification.
Should not have
• Playfulness

```html
<!DOCTYPE html>
<html lang="en">
<head>
<meta charset="utf-8">
<title>Brightwater Herbalist – Naturopathic Food Supplement Label</title>
<link href="https://fonts.googleapis.com/css2?family=Archivo+Black&family=Arimo:ital,wght@0,400;0,700;1,400;1,700&display=swap" rel="stylesheet">
<style>
  :root{
    --backdrop:#efefef;
    --orange:#f7941d;
    --orange-deep:#ef7d12;
    --yellow:#ffd21f;
    --yellow-light:#fff3a0;
    --brown:#7a3a12;
    --ink:#1a1a1a;
    --ink-soft:#3b3b3b;
    --paper:#ffffff;
    --leaf:#5a9a1c;
  }
  *{box-sizing:border-box;margin:0;padding:0}
  html,body{width:1200px;height:746px;overflow:hidden}
  body{background:var(--backdrop);font-family:"Arimo",sans-serif;color:var(--ink)}
  .label{
    position:absolute;left:40px;top:178px;width:1120px;height:390px;
    display:grid;grid-template-columns:373px 374px 373px;
    background:linear-gradient(90deg,var(--orange-deep),var(--orange) 50%,var(--orange-deep));
    box-shadow:0 10px 30px rgba(0,0,0,.18);
  }
  .panel{position:relative;padding:26px 22px;overflow:hidden}
  /* back panel */
  .directions{background:var(--paper);padding:8px 10px;font-size:10.5px;line-height:1.35;color:var(--orange-deep)}
  .directions p+p{margin-top:8px}
  .directions strong{font-weight:700}
  .warning{margin-top:12px;font-weight:700;font-style:italic;font-size:12.5px;line-height:1.3;color:var(--ink)}
  .statement{margin-top:12px;background:var(--paper);padding:6px 10px;font-size:10px;line-height:1.35;color:var(--orange-deep)}
  .maker{position:absolute;left:42px;bottom:52px;font-weight:700;font-style:italic;font-size:12.5px;line-height:1.3}
  .brand{position:absolute;display:flex;align-items:center;gap:6px;font-weight:700;font-size:11px;letter-spacing:.04em;color:var(--brown)}
  .brand::before{content:"";width:12px;height:12px;border-radius:50%;background:var(--leaf)}
  .panel-back .brand{left:180px;bottom:48px}
  /* front panel */
  .panel-front{padding:0}
  .front-art{position:absolute;inset:0;
    background:
      radial-gradient(ellipse 60px 260px at 50% 100%,var(--yellow-light),transparent 70%),
      radial-gradient(ellipse 170px 220px at 50% 30%,var(--yellow),transparent 75%),
      linear-gradient(90deg,var(--orange-deep),var(--orange) 30%,var(--orange) 70%,var(--orange-deep));}
  .front-content{position:relative;padding-top:58px;text-align:center}
  .product-name{font-family:"Archivo Black",sans-serif;font-size:38px;letter-spacing:-.5px;color:var(--brown);
    -webkit-text-stroke:1.5px var(--paper);paint-order:stroke fill}
  .product-type{margin-top:-4px;font-weight:700;font-style:italic;font-size:25px;color:var(--brown)}
  .tag{display:inline-block;margin-top:10px;padding:4px 20px;border-radius:14px;background:var(--orange-deep);
    color:var(--paper);font-weight:700;font-size:14px}
  .benefits{position:absolute;left:26px;top:270px;list-style:none;font-weight:700;font-style:italic;font-size:13px;line-height:1.3;color:#5c3a1a}
  .panel-front .brand{right:18px;top:314px}
  /* facts panel */
  .facts{background:var(--paper);margin-left:30px;padding:6px 8px;font-size:8.5px;color:var(--ink)}
  .facts h2{font-family:"Archivo Black",sans-serif;font-size:19px;letter-spacing:.3px;line-height:1}
  .facts .meta{margin-top:2px;line-height:1.25;border-bottom:4px solid var(--ink);padding-bottom:2px}
  .facts table{width:100%;border-collapse:collapse}
  .facts th{font-weight:700;text-align:right;padding:2px 0;border-bottom:2px solid var(--ink)}
  .facts th:first-child{text-align:center}
  .facts td{padding:2px 0;border-bottom:1px solid var(--ink-soft);vertical-align:top}
  .facts td.amt{text-align:right;white-space:nowrap;padding-left:6px}
  .facts td.dv{text-align:right;width:26px}
  .facts .notes{margin-top:4px;border-top:3px solid var(--ink);padding-top:3px;line-height:1.3}
</style>
</head>
<body>
<main class="label">

  <section class="panel panel-back">
    <div class="directions">
      <p><strong>SUGGESTED USE:</strong> As a dietary supplement, take one (1) veggie capsule three times daily with a full glass of water, ideally 30-60 minutes before each meal.</p>
      <p><strong>CAUTION:</strong> Do not exceed the recommended dose. Pregnant or nursing mothers, children under 18 and people with a known medical condition should consult a physician before using this or any other dietary supplement.</p>
    </div>
    <p class="warning">Keep out of the reach of the children,<br>do not used if the safety seal damaged<br>or missing, store in a cool and dry place.</p>
    <p class="statement">These statements have not been evaluated by the Food and Drug Administration. This product is not intended to diagnose, treat, cure or prevent any disease.</p>
    <p class="maker">Manufactured by<br>Lorem Ipsum</p>
    <p class="brand">BRIGHTWATER HERBALIST</p>
  </section>

  <section class="panel panel-front">
    <div class="front-art" role="img" aria-label="Flowing yellow and orange light swirls rising from the base of the label"></div>
    <div class="front-content">
      <h1 class="product-name">NATUROPATHIC</h1>
      <p class="product-type">food supplement</p>
      <p class="tag">SUPER FOOD</p>
    </div>
    <ul class="benefits">
      <li>Natural weight loss</li>
      <li>Vitamins</li>
      <li>Herbs</li>
      <li>Alkalizing</li>
      <li>Amino acids</li>
    </ul>
    <p class="brand">BRIGHTWATER HERBALIST</p>
  </section>

  <section class="panel panel-facts">
    <div class="facts">
      <h2>SUPPLEMENT FACTS</h2>
      <p class="meta">Serving Size: 1 veggie capsule<br>Servings Per Container: 90</p>
      <table>
        <tr><th>Amount Per Serving</th><th colspan="2">%Daily Value</th></tr>
        <tr><td>Garcinia Cambogia Extract (standardized to 60% Hydroxycitric Acid)</td><td class="amt">500 mg</td><td class="dv">**</td></tr>
        <tr><td>Raspberry Ketones</td><td class="amt">150 mg</td><td class="dv">**</td></tr>
        <tr><td>Calcium</td><td class="amt">50 mg</td><td class="dv">5%</td></tr>
      </table>
      <p class="notes">% Daily Value based on a 2000 calorie diet<br>** Daily Value not established</p>
    </div>
  </section>

</main>
</body>
</html>
```